Business Card Design Project

I own a dental practice and would like to use a logo that was recently designed to make business cards.
I am looking for a clean card with the following information on the card.

Halvorsen Dental Center (Using the logo)
Martin L. Halvorsen, D.D.S.
7234 Pinewick Ave. Suite B
Colorado Springs, CO 80547
(719) 482-6130
halvorsendentalcenter@mailbox-example.net
www.halvorsendentalcenter.example

Also a list of items on the back:
Services include

Family Dentistry
Cosmetic
Whitening
Tooth Colored Fillings
Crowns/Bridges
Implants/Tooth Replacement
Dentures
Root Canals
Updates

Just an FYI, I added an email address and website address.

I also added my Pic.  Please give designs with and without the pic

Thanks

Target Market(s)

20-70 U.S. Female that handles the household budget.

Industry/Entity Type

Dental

Requirements
Must have
• The logo is key. The color scheme of the logo is also key. The back of the business card should have the list of Dental Services offered at the practice. The front should be clean and professional looking. No cartoons. I will also include a picture of myself. I think that the final card may or may not include this picture, so the card designs should come with and without the picture. USE THE BLUE LOGO ONLY!!!
Should not have
• NO teeth should be on the card.

```html
<!DOCTYPE html>
<html lang="en">
<head>
<meta charset="utf-8">
<title>Halvorsen Dental Center – Business Cards</title>
<link href="https://fonts.googleapis.com/css2?family=Open+Sans:wght@400;600;700&display=swap" rel="stylesheet">
<style>
  :root {
    --page-bg: #e9e6e2;
    --card-bg: #ffffff;
    --teal: #3f7389;
    --teal-dark: #1e4a5d;
    --teal-light: #5f95aa;
    --warm-gray: #6b6266;
    --text-gray: #4a4548;
    --rule: #9a9497;
    --soft-gray: #8d8a8c;
  }
  * { box-sizing: border-box; margin: 0; padding: 0; }
  html, body {
    width: 1200px; height: 1024px; overflow: hidden;
    background: var(--page-bg);
    font-family: "Open Sans", Arial, sans-serif;
    color: var(--text-gray);
  }
  .sheet {
    position: relative; width: 1200px; height: 1024px;
  }
  .card {
    position: absolute; left: 180px; width: 840px; height: 480px;
    background: var(--card-bg);
    box-shadow: 0 6px 18px rgba(0,0,0,0.18);
    overflow: hidden;
  }
  .card--front { top: 24px; }
  .card--back { top: 520px; }

  .card__band {
    position: absolute; left: 0; right: 0; bottom: 0; height: 66px;
    background: linear-gradient(90deg, var(--teal-dark), var(--teal-light) 55%, var(--teal-dark));
    border-top: 7px solid var(--warm-gray);
    display: flex; align-items: center; justify-content: flex-end;
    padding-right: 40px;
  }
  .card__website {
    color: #fff; font-size: 19px; letter-spacing: 0.3px;
  }

  /* Front */
  .portrait {
    position: absolute; right: 0; top: 0; width: 380px; height: 250px;
    background: linear-gradient(110deg, #ffffff 0%, #f1eeee 18%, #c9a58f 30%, #2c2a2d 52%, #1b1a1d 100%);
  }
  .wordmark {
    position: absolute; left: 52px; top: 140px;
    display: flex; align-items: center; gap: 14px;
  }
  .wordmark__dot {
    width: 42px; height: 42px; border-radius: 50%; background: var(--teal);
  }
  .wordmark__name {
    font-size: 30px; font-weight: 600; color: var(--teal); line-height: 1.1;
  }
  .wordmark__tagline {
    font-size: 13px; letter-spacing: 2px; color: var(--warm-gray); margin-top: 4px;
  }
  .contact {
    position: absolute; left: 52px; top: 232px;
  }
  .contact__name {
    font-size: 21px; font-weight: 700; color: var(--teal); letter-spacing: 0.3px;
    margin-bottom: 6px;
  }
  .contact__name span { color: var(--warm-gray); font-weight: 400; }
  .contact__name b { color: var(--text-gray); }
  .contact__line {
    font-size: 17px; line-height: 25px; color: var(--text-gray);
    display: flex; align-items: center; gap: 8px;
  }
  .contact__line svg { flex: none; }

  /* Back */
  .appointment {
    position: absolute; left: 44px; top: 34px; width: 420px;
  }
  .appointment__title { font-size: 18px; color: var(--text-gray); margin-bottom: 10px; }
  .appointment__field {
    display: flex; align-items: flex-end; height: 44px; font-size: 18px;
  }
  .appointment__field span { width: 60px; }
  .appointment__field i {
    flex: 1; border-bottom: 1.5px solid var(--rule); height: 30px;
  }
  .back-wordmark {
    position: absolute; left: 500px; top: 120px;
  }
  .back-wordmark .wordmark__name { font-size: 27px; }
  .services {
    position: absolute; left: 44px; top: 300px; right: 30px;
    font-size: 18px; line-height: 34px; color: var(--text-gray);
  }
  .services__row { display: flex; align-items: center; flex-wrap: wrap; }
  .services__item { display: inline-flex; align-items: center; margin-right: 10px; }
  .services__item::before {
    content: ""; width: 9px; height: 9px; border-radius: 50%;
    background: var(--teal); margin-right: 8px;
  }
  .services__item:first-child::before { display: none; }
</style>
</head>
<body>
<main class="sheet">

  <section class="card card--front" aria-label="Business card front">
    <div class="portrait" role="img" aria-label="Portrait photo of Dr. Martin L. Halvorsen in a dark suit"></div>

    <div class="wordmark">
      <div class="wordmark__dot"></div>
      <div>
        <div class="wordmark__name">Halvorsen Dental Center</div>
        <div class="wordmark__tagline">FAMILY · COSMETIC · IMPLANTS</div>
      </div>
    </div>

    <div class="contact">
      <div class="contact__name">MARTIN L. HALVORSEN <span>|</span> <b>D.D.S.</b></div>
      <div class="contact__line">7234 Pinewick Ave. Suite B</div>
      <div class="contact__line">Colorado Springs, CO 80547</div>
      <div class="contact__line">
        <svg width="16" height="16" viewBox="0 0 24 24" aria-hidden="true"><path fill="#4a4548" d="M6.6 10.8a15.2 15.2 0 0 0 6.6 6.6l2.2-2.2a1 1 0 0 1 1-.25 11.4 11.4 0 0 0 3.6.57 1 1 0 0 1 1 1V20a1 1 0 0 1-1 1A17 17 0 0 1 3 4a1 1 0 0 1 1-1h3.5a1 1 0 0 1 1 1c0 1.25.2 2.45.57 3.57a1 1 0 0 1-.25 1z"/></svg>
        (719) 482-6130
      </div>
      <div class="contact__line">
        <svg width="16" height="14" viewBox="0 0 24 18" aria-hidden="true"><rect x="1" y="1" width="22" height="16" rx="1" fill="#4a4548"/><path d="M2 2l10 8 10-8" fill="none" stroke="#fff" stroke-width="1.6"/></svg>
        halvorsendentalcenter@mailbox-example.net
      </div>
    </div>

    <div class="card__band"><span class="card__website">www.halvorsendentalcenter.example</span></div>
  </section>

  <section class="card card--back" aria-label="Business card back">
    <div class="appointment">
      <div class="appointment__title">Appointment</div>
      <div class="appointment__field"><span>For:</span><i></i></div>
      <div class="appointment__field"><span>Day:</span><i></i></div>
      <div class="appointment__field"><span>Date:</span><i></i></div>
      <div class="appointment__field"><span>Time:</span><i></i></div>
    </div>

    <div class="wordmark back-wordmark">
      <div class="wordmark__dot"></div>
      <div>
        <div class="wordmark__name">Halvorsen Dental Center</div>
        <div class="wordmark__tagline">FAMILY · COSMETIC · IMPLANTS</div>
      </div>
    </div>

    <div class="services">
      <div class="services__row">
        <span class="services__item">Family Dentistry</span>
        <span class="services__item">Cosmetic</span>
        <span class="services__item">Whitening</span>
        <span class="services__item">Tooth Colored Fillings</span>
      </div>
      <div class="services__row">
        <span class="services__item">Crowns/Bridges</span>
        <span class="services__item">Implants/Tooth Replacement</span>
        <span class="services__item">Dentures</span>
        <span class="services__item">Root Canals</span>
      </div>
    </div>

    <div class="card__band"><span class="card__website">www.halvorsendentalcenter.example</span></div>
  </section>

</main>
</body>
</html>
```